We need 3 A2 posters similar look but different enough to be eye catching when changed.

We are a healthcare centre that requires 3 A2 posters - simple, similar but different background colours. These posters will be used within our business to promote services we provide to our clients.

The design should include our logo(attached), a large header and a large section in the middle of the poster to promote the event. We need a blank text box (which WE can insert text to advertise), and 1 image to advertise the event. Please note, we do not need you to choose an image we simply would like you to place a demo to give us an idea of where it should sit.

We want to use the bubble design (attached) as a background and the company colours pink, orange and blue - as on our website. Attached is a copy of our logo and background bubble effect. You can also refer to our website - www.tallowbrookwellness.com.au for more inspiration.

Just to reiterate, these posters should be simple, different but have a uniform feel. They should have an empty middle section that can be edited to add text and a space for an eye catching title and matching image.

Our services include Chiropractic, Podiatry, Nutrition, Massage, Yoga, Pilates and Specialised rehabilitation classes.

Reason: Hi designers, I know we are all busy but I really need more designs from the designers I invited to this project and look forward to receiving more designs. Any questions please let me know. Regards, Marlene

Reason: Hi all Increased the budget Regards Marlene

Target Market(s)

Corporate Sydney City office workers

Industry/Entity Type

Healthcare

Requirements
Must have
• logo and company colours
section in the middles that can be edited to add text
Space allocated for image placement
Catchy title/header

```html
<!DOCTYPE html>
<html lang="en">
<head>
<meta charset="utf-8">
<title>Tallowbrook Wellness – Poster</title>
<link href="https://fonts.googleapis.com/css2?family=Poppins:wght@600;700&display=swap" rel="stylesheet">
<style>
  :root {
    --page: #ffffff;
    --sky: #a9c3f3;
    --sky-light: #bcd2f7;
    --blue: #5b7ff2;
    --orange: #d98e3c;
    --magenta: #c132e0;
    --white: #ffffff;
    --photo-a: #e8edf4;
    --photo-b: #c9d6ea;
    --photo-c: #9fb3d8;
  }
  * { box-sizing: border-box; margin: 0; padding: 0; }
  html, body {
    width: 908px; height: 1200px; overflow: hidden;
    background: var(--page);
    font-family: "Poppins", "Century Gothic", sans-serif;
  }
  .poster {
    position: absolute; left: 71px; top: 56px;
    width: 757px; height: 1071px;
    background: linear-gradient(160deg, var(--sky-light) 0%, var(--sky) 55%, var(--sky-light) 100%);
    overflow: hidden;
  }
  .top-strip {
    position: absolute; left: 0; top: 0; width: 757px; height: 19px;
    background: var(--blue);
  }
  .top-strip .accent-orange {
    position: absolute; left: 526px; top: 2px; width: 69px; height: 17px;
    background: var(--orange);
  }
  .top-strip .accent-magenta {
    position: absolute; left: 595px; top: 2px; width: 162px; height: 17px;
    background: var(--magenta);
  }
  .header-bar {
    position: absolute; left: 26px; top: 19px; width: 701px; height: 110px;
    background: var(--blue);
    border-radius: 0 0 12px 12px;
    box-shadow: 0 3px 8px rgba(40, 60, 140, 0.2);
  }
  .header-title {
    position: absolute; right: 26px; top: 38px;
    color: var(--white);
    font-size: 43px; font-weight: 600; line-height: 1;
    letter-spacing: 0.2px;
  }
  .content-box {
    position: absolute; left: 86px; top: 365px; width: 594px; height: 574px;
    background: var(--white);
    border: 4px solid var(--blue);
    border-radius: 14px;
    box-shadow: 0 4px 12px rgba(40, 60, 140, 0.25);
  }
  .content-text {
    position: absolute; left: 11px; top: 142px; width: 575px;
    color: var(--blue);
    font-size: 19px; font-weight: 600; line-height: 27px;
  }
  .content-text p + p { margin-top: 27px; }
  .event-image {
    position: absolute; left: 381px; top: 158px; width: 348px; height: 318px;
    border: 3px solid var(--blue);
    border-radius: 14px;
    overflow: hidden;
    box-shadow: 0 4px 12px rgba(40, 60, 140, 0.25);
  }
  .event-image svg { display: block; }
  .web-address {
    position: absolute; right: 21px; top: 958px;
    color: var(--white);
    font-size: 19px; font-weight: 600; line-height: 1;
  }
  .footer-band {
    position: absolute; left: 0; top: 990px; width: 757px; height: 81px;
    background: var(--magenta);
  }
  .brand {
    position: absolute; right: 26px; top: 24px;
    display: flex; align-items: center; gap: 10px;
    color: var(--white);
    font-size: 28px; font-weight: 700; line-height: 1;
  }
  .brand-square {
    width: 22px; height: 22px; background: var(--white);
  }
</style>
</head>
<body>
  <main class="poster">
    <div class="top-strip">
      <span class="accent-orange"></span>
      <span class="accent-magenta"></span>
    </div>

    <header class="header-bar">
      <h1 class="header-title">Header text space</h1>
    </header>

    <section class="content-box">
      <div class="content-text">
        <p>Welcome to Tallowbrook Wellness. Our goal is to achieve the best possible health outcome for our patients. Our unique combination of therapies, structural correction and individualised exercise programs is what sets us apart.</p>
        <p>At anytime, if you have a health condition, even if you feel it is not something we could help you with, contact us and we will find the right solution for you. We are here for the health of our community"</p>
      </div>
    </section>

    <figure class="event-image">
      <svg width="342" height="312" viewBox="0 0 342 312" role="img" aria-label="Event image placeholder: a mother and daughter preparing fresh vegetables together in a bright kitchen">
        <defs>
          <linearGradient id="eventImageTone" x1="0" y1="0" x2="0" y2="1">
            <stop offset="0" stop-color="var(--photo-a)"/>
            <stop offset="0.6" stop-color="var(--photo-b)"/>
            <stop offset="1" stop-color="var(--photo-c)"/>
          </linearGradient>
        </defs>
        <rect width="342" height="312" fill="url(#eventImageTone)"/>
      </svg>
    </figure>

    <p class="web-address">www.tallowbrookwellness.com.au</p>

    <footer class="footer-band">
      <div class="brand">
        <span class="brand-square"></span>
        <span class="brand-name">Tallowbrook Wellness</span>
      </div>
    </footer>
  </main>
</body>
</html>
```